PSD Website Design

I am looking to have a custom website designed. I would like a PSD made of the design I came up with. Once I get the design I will slice the PSD and create a wordpress template from it.

See attachment for basic layout of the graphic. The image labeled Player page is the basic page I will need for the website. I also need a home page with an image slider on it and thumbnails of recent, state video uploads.

A textured background is ok.

Looking for a quick turnaround.

Text at top of page is a menu that is needed. Open to seeing the menu as a navigational bar or/and with different font types.

No preference on page background color or font colors. I welcome creativity.

```html
<!DOCTYPE html>
<html lang="en">
<head>
<meta charset="utf-8">
<title>Summit Athletic Scouting – Player Page</title>
<link href="https://fonts.googleapis.com/css2?family=Oswald:wght@400;600&family=Open+Sans:wght@400;600;700&display=swap" rel="stylesheet">
<style>
:root{
  --orange:#ef8420;
  --ink:#2c2c2c;
  --muted:#7a7a7a;
  --page:#e9e9e9;
  --panel:#ffffff;
  --ribbon:#c9272c;
  --green:#79b83a;
  --teal:#4db3c8;
  --foot:#3b3b3b;
  --foot-deep:#262626;
  --line:#d6d6d6;
  --thumb-a:#7d8f6a;
  --thumb-b:#b9b1a0;
}
*{box-sizing:border-box;margin:0;padding:0}
html,body{width:843px;height:1200px;overflow:hidden}
body{background:var(--page);font-family:"Open Sans",Arial,sans-serif;color:var(--ink);position:relative}
.abs{position:absolute}

/* header */
.site-header{left:0;top:0;width:843px;height:58px;background:var(--panel);border-bottom:1px solid var(--line)}
.brand{left:22px;top:6px;color:var(--ink);font-family:"Oswald",sans-serif;font-weight:600;line-height:1}
.brand-name{font-size:30px;letter-spacing:1px;display:block}
.brand-tag{font-size:9px;letter-spacing:1.5px;display:block;margin-top:2px}
.main-nav{left:312px;top:18px;display:flex;gap:22px;font-size:16px;color:var(--muted)}
.main-nav a{color:inherit;text-decoration:none;padding-bottom:6px}
.main-nav a.active{color:var(--orange);font-weight:600;border-bottom:3px solid var(--orange)}
.search{left:690px;top:16px;width:130px;height:22px;border:1px solid var(--line);background:#f6f6f6}
.search svg{position:absolute;right:4px;top:3px}

/* page panel */
.content{left:14px;top:64px;width:815px;height:928px;background:var(--panel)}

/* profile */
.photo{left:30px;top:64px;width:190px;height:200px;background:linear-gradient(160deg,#d7d7d7,#9aa9b5);border:6px solid #fff;box-shadow:0 2px 6px rgba(0,0,0,.35);transform:rotate(-3deg)}
.player-name{left:244px;top:80px;font-size:25px;font-weight:700}
.player-facts{left:244px;top:114px;font-size:11.5px;line-height:16px;color:#444}
.player-facts .pos{color:var(--orange);font-weight:600}
.class-year{left:40px;top:272px;font-family:"Oswald",sans-serif;font-size:15px;color:var(--orange)}

/* game film */
.film-rule{left:430px;top:102px;width:390px;height:2px;background:var(--ribbon)}
.film-ribbon{left:530px;top:88px}
.thumb-grid{display:grid;grid-template-columns:repeat(3,120px);gap:8px 10px}
.thumb .pic{height:48px;background:linear-gradient(135deg,var(--thumb-a),var(--thumb-b))}
.thumb .cap{font-size:8.5px;line-height:11px;margin-top:3px;color:#1f5fa8}
.thumb .meta{font-size:7.5px;color:var(--muted)}
.film-grid{left:436px;top:116px}
.channel{display:flex;align-items:center;gap:6px;font-size:8.5px;font-weight:600}
.channel i{width:12px;height:12px;background:#999;border-radius:50%;display:inline-block}
.film-channel{left:436px;top:276px}
.film-grid-2{left:436px;top:294px}
.thumb.cartoon .pic{background:linear-gradient(135deg,#c44b3d,#3f7fc2)}

/* section headings */
.sec-head{font-family:"Oswald",sans-serif;font-size:18px;color:var(--orange);display:flex;align-items:center;gap:8px}
.sec-head::after{content:"";flex:1;height:2px;background:var(--line)}
.highlights-head{left:28px;top:368px;width:470px}
.highlights-head::before{content:"";width:30px;height:2px;background:var(--line);order:-1}

/* highlight video */
.video{left:26px;top:402px;width:476px;height:316px;background:linear-gradient(180deg,#b5c3cf 0%,#8a8f86 45%,#6f8a52 100%);border:1px solid #999}
.video-bar{left:26px;top:698px;width:476px;height:20px;background:rgba(0,0,0,.75)}
.video-bar svg{position:absolute;left:8px;top:5px}
.video-bar .track{position:absolute;left:26px;top:9px;width:380px;height:3px;background:#777}
.video-bar .track::before{content:"";position:absolute;left:0;top:0;width:120px;height:3px;background:var(--ribbon)}

.ad-spot{left:516px;top:402px;width:304px;height:288px;background:#bdbdbd;display:flex;align-items:center;justify-content:center;font-family:"Oswald",sans-serif;font-size:25px;color:#fff;letter-spacing:.5px}

/* recruits tabs */
.tabs{left:26px;top:736px;width:476px;display:flex;gap:6px;border-bottom:2px solid var(--green)}
.tab{font-family:"Oswald",sans-serif;font-size:13px;padding:5px 14px;border-radius:4px 4px 0 0}
.tab.current{color:var(--orange);border:1px solid var(--line);border-bottom:none;background:#fff}
.tab.alt{background:var(--green);color:#fff;flex:1;text-align:center}
.recruit-grid{left:30px;top:772px;grid-template-columns:repeat(4,110px);gap:8px 10px}
.recruit-channel{left:30px;top:850px}
.recruit-grid-2{left:30px;top:866px;grid-template-columns:repeat(4,110px);gap:8px 10px}

/* right column */
.viral-head{left:516px;top:736px;width:304px}
.viral-head::before{content:"";width:24px;height:2px;background:var(--line);order:-1}
.next-event{left:516px;top:758px;width:304px;height:86px;background:#1e1e1e;color:#fff;padding:7px 10px}
.next-event h3{font-family:"Oswald",sans-serif;font-weight:600;font-size:16px;margin-bottom:3px}
.next-event p{font-size:10px;line-height:13px}
.connect{left:516px;top:850px;width:304px;height:26px;background:var(--teal);color:#fff;font-family:"Oswald",sans-serif;font-size:14px;text-align:center;line-height:26px}
.social{left:540px;top:888px;display:flex;gap:14px}
.social span{width:54px;height:54px;border-radius:8px;display:block}

/* footer */
.site-footer{left:0;top:996px;width:843px;height:182px;background:var(--foot);border-top:6px solid var(--orange)}
.foot-col{top:1014px;color:#ddd;font-size:12px}
.foot-col h4{font-family:"Oswald",sans-serif;font-weight:400;font-size:17px;color:var(--orange);margin-bottom:10px}
.foot-col li{list-style:none;line-height:22px}
.quick{left:26px}
.contact{left:296px}
.contact li{display:flex;align-items:center;gap:8px;line-height:26px}
.touch{left:520px;width:300px}
.touch .row{display:flex;gap:6px;margin-bottom:6px}
.touch .field{height:20px;background:#8a8a8a;color:#fff;font-size:10px;padding:3px 6px;flex:1}
.touch .msg{height:46px;background:#8a8a8a;color:#fff;font-size:10px;padding:4px 6px}
.touch .send{margin:6px 0 0 auto;width:54px;height:20px;background:var(--orange);color:#fff;font-size:10px;text-align:center;line-height:20px}
.copyright{left:0;top:1178px;width:843px;height:22px;background:var(--foot-deep);color:#aaa;font-size:10px;line-height:22px;padding-left:26px}
</style>
</head>
<body>

<header class="site-header abs">
  <div class="brand abs"><span class="brand-name">SUMMIT</span><span class="brand-tag">ATHLETIC SCOUTING</span></div>
  <nav class="main-nav abs">
    <a href="#">Home</a><a href="#">About us</a><a href="#">State</a><a href="#" class="active">Position</a><a href="#">Join</a>
  </nav>
  <div class="search abs"><svg width="14" height="14" viewBox="0 0 14 14"><circle cx="6" cy="6" r="4" fill="none" stroke="#777" stroke-width="1.6"/><line x1="9" y1="9" x2="13" y2="13" stroke="#777" stroke-width="1.8"/></svg></div>
</header>

<main>
  <div class="content abs"></div>

  <section class="profile">
    <div class="photo abs" role="img" aria-label="Player portrait photo"></div>
    <h1 class="player-name abs">Marcus Delaney</h1>
    <div class="player-facts abs">
      <div class="pos">Wide Receiver</div>
      <div>Miami, FL (North Central)</div>
      <div>Ht: 6'1 | Wt: 187</div>
      <div>40 Time: 4.40</div>
      <div>Bench: 225 lbs</div>
      <div>Vertical: 36</div>
      <div>3.4 GPA | 24 ACT</div>
    </div>
    <div class="class-year abs">CLASS OF 2015</div>
  </section>

  <section class="game-film">
    <div class="film-rule abs"></div>
    <svg class="film-ribbon abs" width="150" height="34" viewBox="0 0 150 34">
      <polygon points="0,6 12,6 12,28 0,28 6,17" fill="#9e1d21"/>
      <polygon points="150,6 138,6 138,28 150,28 144,17" fill="#9e1d21"/>
      <rect x="10" y="0" width="130" height="30" fill="#c9272c"/>
      <text x="75" y="21" text-anchor="middle" fill="#fff" font-family="Oswald, sans-serif" font-size="16" font-weight="600">GAME FILM</text>
    </svg>
    <div class="thumb-grid film-grid abs">
      <div class="thumb"><div class="pic" role="img" aria-label="Game video still"></div><div class="cap">Spring Camp Drills</div><div class="meta">1,204 views</div></div>
      <div class="thumb"><div class="pic" role="img" aria-label="Game video still"></div><div class="cap">Route Running Reel</div><div class="meta">986 views</div></div>
      <div class="thumb"><div class="pic" role="img" aria-label="Game video still"></div><div class="cap">Senior Season Week 3</div><div class="meta">2,310 views</div></div>
      <div class="thumb"><div class="pic" role="img" aria-label="Game video still"></div><div class="cap">Combine Speed Test</div><div class="meta">745 views</div></div>
      <div class="thumb"><div class="pic" role="img" aria-label="Game video still"></div><div class="cap">Playoff Touchdown</div><div class="meta">3,122 views</div></div>
      <div class="thumb"><div class="pic" role="img" aria-label="Game video still"></div><div class="cap">Catching Drills</div><div class="meta">612 views</div></div>
    </div>
    <div class="channel film-channel abs"><i></i>Team Channel</div>
    <div class="thumb-grid film-grid-2 abs">
      <div class="thumb cartoon"><div class="pic" role="img" aria-label="Video still"></div><div class="cap">Weekly Recap Show</div></div>
      <div class="thumb cartoon"><div class="pic" role="img" aria-label="Video still"></div><div class="cap">Highlights of the Week</div></div>
      <div class="thumb cartoon"><div class="pic" role="img" aria-label="Video still"></div><div class="cap">Top Ten Catches</div></div>
    </div>
  </section>

  <section class="highlights">
    <h2 class="sec-head highlights-head abs">HIGHLIGHTS</h2>
    <div class="video abs" role="img" aria-label="Highlight video of players on the field"></div>
    <div class="video-bar abs">
      <svg width="10" height="10" viewBox="0 0 10 10"><polygon points="0,0 10,5 0,10" fill="#fff"/></svg>
      <span class="track"></span>
    </div>
    <div class="ad-spot abs">ADVERTISEMENT SPOT</div>
  </section>

  <section class="recruits">
    <div class="tabs abs">
      <span class="tab current">RECENT RECRUITS</span>
      <span class="tab alt">FLORIDA</span>
      <span class="tab alt">MOST VIEWED</span>
    </div>
    <div class="thumb-grid recruit-grid abs">
      <div class="thumb"><div class="pic" role="img" aria-label="Recruit video still"></div><div class="cap">QB Camp Session</div></div>
      <div class="thumb"><div class="pic" role="img" aria-label="Recruit video still"></div><div class="cap">Linebacker Film</div></div>
      <div class="thumb"><div class="pic" role="img" aria-label="Recruit video still"></div><div class="cap">Junior Season Reel</div></div>
      <div class="thumb"><div class="pic" role="img" aria-label="Recruit video still"></div><div class="cap">Kick Return Tape</div></div>
    </div>
    <div class="channel recruit-channel abs"><i></i>Recruit Channel</div>
    <div class="thumb-grid recruit-grid-2 abs">
      <div class="thumb cartoon"><div class="pic" role="img" aria-label="Video still"></div><div class="cap">Friday Night Recap</div></div>
      <div class="thumb cartoon"><div class="pic" role="img" aria-label="Video still"></div><div class="cap">State Finals Preview</div></div>
      <div class="thumb cartoon"><div class="pic" role="img" aria-label="Video still"></div><div class="cap">Coach Interview</div></div>
      <div class="thumb cartoon"><div class="pic" role="img" aria-label="Video still"></div><div class="cap">Training Day Vlog</div></div>
    </div>
  </section>

  <aside class="viral">
    <h2 class="sec-head viral-head abs">TAKE IT VIRAL</h2>
    <div class="next-event abs">
      <h3>NEXT EVENT</h3>
      <p>Lorem ipsum dolor sit amet, consectetuer adipiscing elit, sed diam nonummy nibh euismod tincidunt ut laoreet dolore magna aliquam erat volutpat.</p>
    </div>
    <div class="connect abs">CONNECT WITH SUMMIT</div>
    <div class="social abs">
      <span style="background:#3b5a9a" role="img" aria-label="Social network link"></span>
      <span style="background:#3fa9dc" role="img" aria-label="Social network link"></span>
      <span style="background:#c4302b" role="img" aria-label="Video network link"></span>
      <span style="background:#8a6a4f" role="img" aria-label="Photo network link"></span>
    </div>
  </aside>
</main>

<footer>
  <div class="site-footer abs"></div>
  <div class="foot-col quick abs">
    <h4>QUICK LINKS</h4>
    <ul><li>About us</li><li>Position</li><li>State</li><li>Join</li></ul>
  </div>
  <div class="foot-col contact abs">
    <h4>CONTACT US</h4>
    <ul>
      <li><svg width="12" height="14" viewBox="0 0 12 14"><path d="M6 0a5 5 0 0 1 5 5c0 4-5 9-5 9S1 9 1 5a5 5 0 0 1 5-5z" fill="#ddd"/><circle cx="6" cy="5" r="2" fill="#3b3b3b"/></svg>Address: 234 Street Name,<br>City, State 01345</li>
      <li><svg width="12" height="14" viewBox="0 0 12 14"><rect x="2" y="0" width="8" height="14" rx="2" fill="#ddd"/><rect x="3.5" y="2" width="5" height="8" fill="#3b3b3b"/></svg>0234 5677 8901</li>
      <li><svg width="14" height="10" viewBox="0 0 14 10"><rect width="14" height="10" fill="#ddd"/><polyline points="0,0 7,6 14,0" fill="none" stroke="#3b3b3b" stroke-width="1.2"/></svg>contact@email.com</li>
    </ul>
  </div>
  <div class="foot-col touch abs">
    <h4>GET IN TOUCH</h4>
    <div class="row"><span class="field">Name</span><span class="field">Email</span></div>
    <div class="msg">Your Message...</div>
    <div class="send">Send</div>
  </div>
  <div class="copyright abs">© 2014 Summit Athletic Scouting, All Rights Reserved</div>
</footer>

</body>
</html>
```